Integrated Health Clinic brochure

We need a brochure designed to highlight the services that we offer at the integrated clinic. Please see "Our Services" of our website for description of services to be added to the brochure except for Acupuncture, which is described below:

"Acupuncture is an ancient Chinese methodology that has been proven to be very effective in many health issues, particularly in relieving pain. It involves the stimulation of acupuncture points on the body to regain the natural balance of the body. Medical Acupuncture is effective in treating a wide variety of conditions including: headaches, neck and back pains, carpal tunnel syndrome, fibromyalgia, asthma, allergies, sinus problems, digestive disorders and many others."

our motto "Relieve, Rejuvenate, Renew"

Services we provide:
Chiropractic
Physiotherapy
Family counselling
Massage Therapy
Acupuncture
Osteopath

Colors are blue and green.

See our website www.solvarahealth.ca

```html
<!DOCTYPE html>
<html lang="en">
<head>
<meta charset="utf-8">
<title>Our Services – Brochure</title>
<link href="https://fonts.googleapis.com/css2?family=PT+Sans:wght@400;700&display=swap" rel="stylesheet">
<style>
  :root{
    --blue:#2a9fcf;
    --blue-dark:#1d86b6;
    --green:#7cc242;
    --green-text:#5aa832;
    --teal-text:#2eb3d6;
    --ink:#4a4a4a;
    --muted:#777;
    --photo-skin:#e7c9b3;
    --photo-teal:#8cc7cf;
  }
  *{margin:0;padding:0;box-sizing:border-box}
  html,body{width:849px;height:1200px;overflow:hidden;background:#fff}
  body{font-family:"PT Sans",Arial,sans-serif;color:var(--ink);position:relative}
  .site-line{position:absolute;left:34px;top:12px;font-size:19px;color:var(--muted)}
  .header-band{position:absolute;left:0;top:48px;width:849px;height:80px;
    background:linear-gradient(90deg,var(--blue-dark),var(--blue) 60%,#5fc0e0);}
  .header-band h1{position:absolute;left:34px;top:8px;font-size:50px;font-weight:400;color:#fff;letter-spacing:.5px}
  .service{position:absolute;left:34px;width:500px;font-size:14.5px;line-height:23px;text-align:justify}
  .service-name{font-size:29px;font-weight:400;color:var(--green-text);letter-spacing:.5px;line-height:23px}
  .chiro{top:150px}
  .massage{top:660px}
  .photo{position:absolute;left:556px;width:266px;border:1px solid #ddd}
  .photo-chiro{top:156px;height:304px;background:linear-gradient(135deg,#f3f6f6,var(--photo-teal) 55%,var(--photo-skin))}
  .photo-massage{top:662px;height:270px;background:linear-gradient(160deg,#fafafa,var(--photo-skin) 60%,#f5efe9)}
  .fees-title{position:absolute;left:34px;font-size:22px;font-weight:400;color:var(--green-text);line-height:30px}
  .fees-chiro{top:496px}
  .fees-list{position:absolute;left:34px;list-style:none;font-size:17px;color:var(--teal-text);line-height:30px}
  .fees-list li::before{content:"* ";color:var(--green)}
  .chiro-prices{top:534px}
  .benefits{position:absolute;left:34px;top:808px;width:500px;list-style:none;font-size:14px;line-height:22px;color:var(--green-text)}
  .benefits li::before{content:"o";margin-right:14px;color:var(--green)}
  .massage-close{position:absolute;left:34px;top:958px;width:500px;font-size:14.5px;line-height:23px;text-align:justify}
  .fees-massage{top:1036px}
  .massage-prices{top:1138px;display:flex;gap:60px}
  .footer-band{position:absolute;left:0;top:1182px;width:849px;height:18px;background:linear-gradient(90deg,var(--blue-dark),var(--blue))}
  .page-number{position:absolute;right:18px;top:1152px;font-size:22px;color:var(--blue-dark);font-weight:700}
</style>
</head>
<body>
  <p class="site-line">Visit our website: www.solvarahealth.ca</p>

  <header class="header-band"><h1>Our Services</h1></header>

  <p class="service chiro"><span class="service-name">CHIROPRACTIC</span> care is a safe, non-invasive, drug-free therapy to correct and prevent joint and muscle pain. By restoring the natural alignment in your body, chiropractic treatments restore movement and prevent potential injuries. Chiropractic treatments are especially effective in treating back, neck, pelvis and joint problems. Procedures most often used are adjustments or spinal manipulative therapy. Adjustments are safe, painless manual procedures where our skilled chiropractors manually apply pressures to your body to restore the natural alignment. Other treatments include various soft tissue techniques, Corvane Technique, elastic taping, Ultrasound among others. Book an appointment now.</p>
  <div class="photo photo-chiro" role="img" aria-label="Chiropractor adjusting a patient's neck"></div>

  <h2 class="fees-title fees-chiro">Chiropractic fees (Covered by most Extended Health Plans)</h2>
  <ul class="fees-list chiro-prices">
    <li>Initial Assessment $90, Seniors 65+ and Students, below 20, $80</li>
    <li>Subsequent visits $50, Seniors and students, $40</li>
  </ul>

  <p class="service massage"><span class="service-name">MASSAGE THERAPY</span> is mostly widely known for its relaxation and stress-release abilities, and it is also recognized as an effective treatment for treating illness and also as a tool in preventative medicine. Safe and effective massage treatments need to be carried out by a Registered Massage Therapist. Benefits of therapeutic massages include:</p>
  <div class="photo photo-massage" role="img" aria-label="Woman receiving a relaxing massage"></div>

  <ul class="benefits">
    <li>Treatment and elimination of chronic pain and acute conditions</li>
    <li>Relaxation and release stress</li>
    <li>Improve circulation</li>
    <li>Improve mobility and balance</li>
    <li>Improve the functioning of immune system</li>
    <li>Lymphatic drainage</li>
  </ul>

  <p class="massage-close">Whether you are looking to get rid of that sore back and leg or looking for improve your golf swing, therapeutic massages can help. Book an appointment now.</p>

  <h2 class="fees-title fees-massage">Massage fees including HST (Registered Massage Therapists)<br>(Covered by most Extended Health Plans)</h2>
  <ul class="fees-list massage-prices">
    <li>30 mins – $60</li>
    <li>1 hour – $90</li>
    <li>90 mins- $130</li>
  </ul>

  <span class="page-number">1</span>
  <footer class="footer-band"></footer>
</body>
</html>
```